Wordpress Design Project for lorettabramwell.com.au

PLEASE NOTE ...Coding Required

I need a simple website to display my art. There will be 4 different categories - FloraGrandis (botanical art), Oceanlife, Travel Sketchbook, Portraits. There needs to be room for an introduction to me and my work,photos of my studio and views from here and a description of each individual piece. I will probably display no more than 10 pieces in category. Obviously I need to change photos on a regular basis.

I would also like to include a Coinvale button to be connected to my Coinvale account.

I have already started to do a website on Wordpress but am finding it too hard to do.

Thank you

Doreen

Reason: I have provided a deadline extension as I feel the initial lead up time could be too short. Hope that helps you. Doreen

Dear designers. Thankyou all so much for submitting some beautiful designs. I will spend time this weekend evaluating them but as the closing date is January 19, I will not make final decisions until then.  You have probably received an update by now butI  just want to mention that Coding is required.

Cheers

Doreen

Thank you Designers for your patience.  I have been advised by PixelHarbor that I cannot make a decision until the deadline has passed, so will let you know on Saturday.

Thank you.
Doreen.

Target Market(s)

35 to 75 who want to buy art and very personal gifts

Industry/Entity Type

Travel

Requirements
Must have
• Ability to change photos often. Modern, elegant, streamlined
Nice to have
• The colour green, an elegant font - sans serif and definitely not courier; room for a photo of me (maybe), and an interesting headline font
Should not have
• quirky, cartooney, retro.

```html
<!DOCTYPE html>
<html lang="en">
<head>
<meta charset="utf-8">
<title>Doreen Ann Bramwell – Art Gallery</title>
<link href="https://fonts.googleapis.com/css2?family=Rokkitt:wght@400;500;600&family=Arimo:wght@400;700&display=swap" rel="stylesheet">
<style>
:root{
  --green:#5b9a2e;
  --green-dark:#4c8424;
  --green-text:#4f8a22;
  --dark:#333333;
  --text:#555;
  --page-bg:#eef0e6;
  --white:#ffffff;
  --grey-line:#d6d6d6;
}
*{box-sizing:border-box;margin:0;padding:0}
html,body{width:1200px;height:1200px;overflow:hidden}
body{background:var(--page-bg);font-family:"Arimo",Arial,sans-serif;color:var(--text);position:relative}
.abs{position:absolute}
.top-bar{left:0;top:0;width:1200px;height:46px;background:linear-gradient(#444,#2e2e2e)}
.account-links{right:92px;top:13px;display:flex;gap:18px;color:#eee;font-size:13px}
.account-links span.sep{color:#bbb}
.account-links .ico{display:inline-block;width:11px;height:11px;margin-right:5px;vertical-align:-1px}
.page{left:90px;top:46px;width:1022px;height:1154px;background:var(--white)}
.social{top:66px;display:flex;align-items:center;gap:4px;font-size:11px}
.social .btn{border:1px solid #c9d3e3;background:#eef2f8;padding:2px 6px;border-radius:2px;color:#3b5a98}
.social .count{border:1px solid #ccc;padding:2px 4px;color:#333;background:#fff}
.social .dot{width:9px;height:9px;background:#7fa4d8;display:inline-block;margin-right:4px}
.search{left:900px;top:63px;width:200px;height:31px;border:2px solid #ddd;border-radius:16px;font-size:11px;color:#aaa;font-style:italic;padding:7px 24px}
.nav{left:90px;top:104px;width:1022px;height:42px;background:linear-gradient(var(--green),var(--green-dark));border-top:2px solid #7db457;border-bottom:2px solid #b9d3a0}
.nav a{position:absolute;top:10px;color:#fff;text-decoration:none;font-family:"Rokkitt",serif;font-size:16px;font-weight:500}
.nav .div{position:absolute;top:8px;width:1px;height:24px;background:#8bbd66}
.site-name{left:400px;top:64px;width:400px;display:flex;justify-content:center;align-items:center;gap:10px;font-family:"Rokkitt",serif;font-weight:600;font-size:28px;color:var(--green-text);line-height:32px}
.site-name i{width:12px;height:12px;background:var(--green);display:block}
.hero{left:99px;top:148px;width:1001px;height:395px;background:linear-gradient(#cfcfcf,#ebebeb 60%,#d9d9d9)}
.hero-deco{left:99px;top:250px;width:120px;height:280px;background:linear-gradient(90deg,rgba(255,255,255,.35),rgba(255,255,255,0))}
.portrait-card{width:211px;height:296px;background:#fff;box-shadow:0 1px 4px rgba(0,0,0,.3)}
.portrait-photo{left:6px;top:5px;width:200px;height:243px;background:linear-gradient(#e8eef3,#b8c3cc 60%,#3a4250)}
.portrait-name{left:0;top:262px;width:211px;text-align:center;font-size:16px;color:#333}
.welcome-title{left:467px;top:236px;font-size:23px;color:var(--green-text);font-weight:400}
.welcome-lead{left:467px;top:280px;width:588px;font-size:13.5px;font-weight:700;color:#333;line-height:23px}
.welcome-body{left:467px;top:334px;width:588px;font-size:13px;line-height:23px;text-align:justify;color:#555}
.slider-tab{left:533px;top:513px;width:134px;height:30px;background:#fff;border-radius:6px 6px 0 0;display:flex;justify-content:center;gap:15px;padding-top:11px}
.slider-tab i{width:11px;height:11px;border-radius:50%;background:#888;display:block}
.slider-tab i.on{background:#8cb86a}
.h2{font-family:"Rokkitt",serif;color:var(--green-text);font-weight:500}
.recent-title{left:100px;top:566px;font-size:24px}
.cats{top:644px;font-family:"Rokkitt",serif;font-size:19px;color:var(--green-text)}
.cats.active{color:#333}
.cat-sep{top:644px;font-size:19px;color:#333}
.arrows{left:1072px;top:647px;display:flex;gap:1px}
.arrows span{width:14px;height:16px;background:#555;border-radius:4px;display:block}
.rule{left:99px;width:1001px;height:1px;background:var(--grey-line)}
.painting-name{top:703px;width:236px;text-align:center;font-size:13px;color:#555}
.thumb{top:728px;width:236px;height:140px;border:4px solid #ddd;background:#fff;box-shadow:0 4px 4px -2px rgba(0,0,0,.15)}
.thumb .art{position:absolute;left:0;top:0;right:0;bottom:0}
.thumb-tools{left:0;bottom:0;width:228px;height:30px;background:rgba(40,40,40,.85);display:flex;justify-content:space-around;align-items:center}
.thumb-tools b{width:10px;height:10px;background:#eee;border-radius:2px;display:block}
.testi-title{left:104px;top:920px;font-size:20px}
.testi-box{left:99px;top:962px;width:1003px;height:102px;background:#f3f3f3;border-radius:8px}
.quote{font-family:"Rokkitt",serif;font-weight:600;font-size:72px;color:#cfcfcf;line-height:72px}
.testi-text{left:75px;top:18px;width:850px;font-size:13px;line-height:21px;color:#444}
.testi-client{right:116px;top:66px;font-size:13px;color:#333}
.footer{left:99px;top:1082px;width:1005px;height:110px;background:#333}
.footer-links{left:15px;top:29px;font-size:13px;color:#eee;word-spacing:2px}
.footer-copy{left:15px;top:63px;font-size:13px;color:#eee}
.pay-name{left:842px;top:16px;font-weight:700;font-size:30px;color:#bbb}
.cards{left:836px;top:66px;display:flex;gap:3px}
.cards span{width:33px;height:20px;background:#e4e4e4;border-radius:2px;display:block}
.page-code{left:1163px;top:1174px;font-size:14px;color:#222}
</style>
</head>
<body>
<header class="abs top-bar">
  <nav class="abs account-links">
    <span><svg class="ico" viewBox="0 0 10 10"><circle cx="5" cy="3" r="2.5" fill="#ddd"/><path d="M0 10 Q5 4 10 10Z" fill="#ddd"/></svg>My Account</span><span class="sep">|</span>
    <span><svg class="ico" viewBox="0 0 10 10"><path d="M0 1h2l1 5h6l1-4H3" stroke="#ddd" fill="none"/><circle cx="4" cy="8.5" r="1" fill="#ddd"/><circle cx="8" cy="8.5" r="1" fill="#ddd"/></svg>My Cart</span><span class="sep">|</span>
    <span><svg class="ico" viewBox="0 0 10 10"><rect x=".5" y=".5" width="9" height="9" fill="none" stroke="#ddd"/><path d="M2 5l2 2 4-5" stroke="#ddd" fill="none" stroke-width="1.5"/></svg>Check out</span><span class="sep">|</span>
    <span><b style="margin-right:4px">?</b>Help</span>
  </nav>
</header>

<div class="abs page"></div>

<div class="abs social" style="left:100px">
  <span class="btn"><span class="dot"></span>Like</span><span class="count">3k</span>
  <span style="width:8px"></span>
  <span class="btn"><span class="dot"></span>Share</span><span class="count">316</span>
</div>
<div class="abs site-name"><i></i>Doreen Ann Bramwell</div>
<div class="abs search">Search
  <svg class="abs" style="right:14px;top:9px" width="11" height="11" viewBox="0 0 11 11"><circle cx="4" cy="4" r="3" stroke="#999" fill="none" stroke-width="1.5"/><path d="M6 6l4 4" stroke="#999" stroke-width="2"/></svg>
</div>

<nav class="abs nav">
  <a style="left:41px">Home</a><span class="div" style="left:106px"></span>
  <a style="left:132px">About me</a><span class="div" style="left:218px"></span>
  <a style="left:245px">Gallery</a>
  <a style="left:710px">My Works</a><span class="div" style="left:806px"></span>
  <a style="left:830px">Blog</a><span class="div" style="left:885px"></span>
  <a style="left:908px">Contact me</a>
</nav>

<section class="abs hero">
  <div class="abs portrait-card" style="left:122px;top:68px">
    <div class="abs portrait-photo" role="img" aria-label="Portrait photo of the artist"></div>
    <div class="abs portrait-name">Doreen Ann Bramwell</div>
  </div>
</section>
<div class="abs hero-deco" role="img" aria-label="Faint botanical sketch decoration"></div>
<h1 class="abs welcome-title">Welcome to my site</h1>
<p class="abs welcome-lead">Welcome to the online gallery of Doreen Ann Bramwell, an artist working in the hills behind beautiful Wattle Cove, NSW&nbsp; Cras gravida laoreet sapien sed egestas.</p>
<p class="abs welcome-body">Pellentesque massa dolor, ultricies at volutpat eu, rhoncus quis mi. Morbi porttitor, libero vel scelerisque rutrum, magna arcu cursus lorem, vitae mattis arcu risus aliquam velit. Nunc dui lectus, euismod faucibus vehicula a, congue et turpis. Morbi hendrerit dapibus pulvinar. Cura bitur sit amet ipsum non orci tempor mattis. Suspendisse dictum placerat consectetur. Etiam euismod, orci a vulputate viverra, dui nibh consequat lectus, eu rutrum orci diam in libero. Nam ut sem nec sem varius scelerisque at a arcu.</p>
<div class="abs slider-tab"><i></i><i></i><i class="on"></i><i></i></div>

<h2 class="abs h2 recent-title">Recent Works</h2>
<svg class="abs" style="left:100px;top:601px" width="147" height="24" viewBox="0 0 147 24"><path d="M2 2 Q2 12 20 12 H62 Q72 12 73.5 22 Q75 12 85 12 H127 Q145 12 145 2" fill="none" stroke="var(--green)" stroke-width="4"/></svg>

<span class="abs cats active" style="left:112px">FloraGrandis</span>
<span class="abs cat-sep" style="left:270px">|</span>
<span class="abs cats" style="left:301px">Oceanlife</span>
<span class="abs cat-sep" style="left:410px">|</span>
<span class="abs cats" style="left:441px">Travel Sketchbook</span>
<span class="abs cat-sep" style="left:629px">|</span>
<span class="abs cats" style="left:660px">Portraits</span>
<div class="abs arrows"><span></span><span></span></div>
<div class="abs rule" style="top:680px"></div>

<div class="abs painting-name" style="left:100px">Painting Name</div>
<div class="abs painting-name" style="left:355px">Painting Name</div>
<div class="abs painting-name" style="left:609px">Painting Name</div>
<div class="abs painting-name" style="left:864px">Painting Name</div>

<div class="abs thumb" style="left:100px">
  <div class="art" role="img" aria-label="Botanical painting of daisies with an insect" style="background:linear-gradient(135deg,#dfe6d8,#b9c7a8 50%,#e9ede2)"></div>
  <div class="abs thumb-tools"><b></b><b style="border-radius:50%"></b><b style="border-radius:50%"></b><b></b><b></b></div>
</div>
<div class="abs thumb" style="left:355px"><div class="art" role="img" aria-label="Botanical painting of pink frangipani flowers and leaves" style="background:linear-gradient(120deg,#4f7a3a,#8fae6e 45%,#f3d8e3 75%,#fff)"></div></div>
<div class="abs thumb" style="left:609px"><div class="art" role="img" aria-label="Botanical painting of purple irises" style="background:radial-gradient(ellipse at 50% 35%,#9a86c4,#c7d3a8 55%,#fff 80%)"></div></div>
<div class="abs thumb" style="left:864px"><div class="art" role="img" aria-label="Botanical painting of red roses" style="background:radial-gradient(ellipse at 45% 40%,#e0505a,#f1b4b0 40%,#fff 75%)"></div></div>

<div class="abs rule" style="top:896px"></div>

<h2 class="abs h2 testi-title">Clients Testimonials</h2>
<section class="abs testi-box">
  <span class="abs quote" style="left:12px;top:6px">&ldquo;</span>
  <p class="abs testi-text">At vero eos et accusamus et iusto odio dignissimos ducimus qui blanditiis praesentium voluptatum deleniti atque corrupti quos dolores et quas molestias excepturi sint occaecati cupiditate non provident, similique.</p>
  <span class="abs testi-client">Client Name, City</span>
  <span class="abs quote" style="right:16px;top:52px">&rdquo;</span>
</section>

<footer class="abs footer">
  <p class="abs footer-links">Home &nbsp;|&nbsp; About us &nbsp;|&nbsp; Gallery &nbsp;|&nbsp; My Works &nbsp;|&nbsp; Blog &nbsp;|&nbsp; Contact us</p>
  <p class="abs footer-copy">Copyright &nbsp;©&nbsp; 2013 &nbsp; www.lorettabramwell.com.au &nbsp;&nbsp; All rights reserved.</p>
  <span class="abs pay-name">Coinvale</span>
  <div class="abs cards"><span></span><span></span><span></span><span></span></div>
</footer>

<span class="abs page-code">M2</span>
</body>
</html>
```